Innovative Healthcare Technology Company needs a Business Card Design

We are in need of an innovative business card design for a new healthcare software company called "Brightwell Harbor Systems". We develop software that creates medical assessment applications and mobile e-learning prevention services to reduce risk behaviors in adolescent and young adults. Our initial product, the "MERIDIAN App", conducts a tailored sexual risk assessment and provides a doctor with an insightful patient report to improve sexual risk counseling and ultimately reduce unintended pregnancy, STDs, etc.

We would like the design to incorporate our logo and branding colors (attached) in an innovative and creative manner. The final design should communicate professionalism and healthcare innovation. Our tag line is "prevention is the solution" (doesn't necessarily need to be included) and our target audience is doctors, medical directors, and medical business administrators. Please visit our website for additional info ourlantrixhub.com. Be creative and we look forward to seeing your designs!

Target Market(s)

healthcare - doctors, medical directors and medical business administrators

Industry/Entity Type

Healthcare

Contact Information for Business Card

We would like the design to incorporate our logo and branding colors (attached) in an innovative and creative manner. The final design should communicate professionalism and healthcare innovation. Our tag line is "prevention is the solution" (doesn't necessarily need to be included)

Font styles to use
Other font styles liked:
• quicksand

Requirements
Must have
• our logo and brand colors
• Name, (Joan Ferraventi, PhD)
• Email (drjoan@ourlantrixhub.com)
• phone (555.213.8870)
• Website (ourlantrixhub.com)
Should not have
• cartoon look

```html
<!DOCTYPE html>
<html lang="en">
<head>
<meta charset="utf-8">
<title>Brightwell Harbor Systems — Business Card</title>
<link rel="stylesheet" href="https://fonts.googleapis.com/css2?family=Didact+Gothic&display=swap">
<style>
  :root {
    --page-bg: #e4e6e8;
    --card-bg: #f4f5f5;
    --brand-blue: #2b4f7a;
    --brand-blue-light: #24557f;
    --brand-blue-dark: #0f2d48;
    --brand-green: #3f7a4f;
    --text-gray: #595b5d;
    --icon-gray: #4f5254;
  }
  * { margin: 0; padding: 0; box-sizing: border-box; }
  html, body {
    width: 1200px;
    height: 970px;
    overflow: hidden;
    background: var(--page-bg);
    font-family: "Didact Gothic", "Century Gothic", sans-serif;
  }
  .canvas {
    position: relative;
    width: 1200px;
    height: 970px;
  }
  .card {
    position: absolute;
    left: 100px;
    top: 207px;
    width: 1000px;
    height: 556px;
    background: var(--card-bg);
    overflow: hidden;
    box-shadow: 0 10px 30px rgba(20, 35, 50, 0.18);
  }
  .card-art {
    position: absolute;
    inset: 0;
    width: 1000px;
    height: 556px;
  }
  .brand {
    position: absolute;
    left: 48px;
    top: 62px;
    display: flex;
    align-items: center;
    gap: 22px;
  }
  .brand-square {
    width: 58px;
    height: 58px;
    background: var(--brand-blue);
  }
  .brand-name {
    font-size: 36px;
    color: var(--brand-blue);
    letter-spacing: 0.5px;
    line-height: 1;
  }
  .person-name {
    position: absolute;
    left: 48px;
    top: 330px;
    font-size: 42px;
    color: var(--text-gray);
    letter-spacing: 0.5px;
    white-space: nowrap;
  }
  .person-name .credential {
    font-size: 32px;
    color: var(--brand-blue);
  }
  .contact-list {
    position: absolute;
    left: 50px;
    top: 396px;
    list-style: none;
  }
  .contact-item {
    display: flex;
    align-items: center;
    gap: 20px;
    height: 47px;
    font-size: 26px;
    color: var(--text-gray);
    letter-spacing: 0.3px;
  }
  .contact-icon {
    width: 32px;
    height: 26px;
    flex: none;
  }
</style>
</head>
<body>
<main class="canvas">
  <section class="card" aria-label="Business card for Joan Ferraventi, Brightwell Harbor Systems">
    <svg class="card-art" viewBox="0 0 1000 556" aria-hidden="true">
      <defs>
        <linearGradient id="blue-panel" x1="0" y1="0" x2="1" y2="1">
          <stop offset="0" stop-color="var(--brand-blue-light)"/>
          <stop offset="1" stop-color="var(--brand-blue-dark)"/>
        </linearGradient>
      </defs>
      <path class="blue-panel" d="M590 0 Q700 278 560 556 L1000 556 L1000 0 Z" fill="url(#blue-panel)"/>
      <path class="green-arc" d="M540 0 Q695 278 530 556 L516 556 Q662 278 528 0 Z" fill="var(--brand-green)"/>
    </svg>

    <div class="brand">
      <span class="brand-square"></span>
      <span class="brand-name">Brightwell Harbor Systems</span>
    </div>

    <h1 class="person-name">Joan Ferraventi, <span class="credential">PhD</span></h1>

    <ul class="contact-list">
      <li class="contact-item">
        <svg class="contact-icon" viewBox="0 0 32 26" aria-hidden="true">
          <rect x="2" y="4" width="28" height="18" fill="var(--icon-gray)"/>
          <path d="M2 4 L16 15 L30 4" fill="none" stroke="var(--card-bg)" stroke-width="2"/>
        </svg>
        drjoan@ourlantrixhub.com
      </li>
      <li class="contact-item">
        <svg class="contact-icon" viewBox="0 0 32 26" aria-hidden="true">
          <path d="M3 9 Q16 0 29 9 L29 12 L23 12 L22 8 Q16 6 10 8 L9 12 L3 12 Z" fill="var(--icon-gray)"/>
          <path d="M9 12 L11 10 L21 10 L23 12 L27 24 L5 24 Z" fill="var(--icon-gray)"/>
          <circle cx="16" cy="17" r="3" fill="var(--card-bg)"/>
        </svg>
        555.213.8870
      </li>
      <li class="contact-item">
        <svg class="contact-icon" viewBox="0 0 32 26" aria-hidden="true">
          <g fill="none" stroke="var(--icon-gray)" stroke-width="2">
            <circle cx="16" cy="13" r="11"/>
            <ellipse cx="16" cy="13" rx="5" ry="11"/>
            <line x1="5" y1="13" x2="27" y2="13"/>
            <path d="M7 7 Q16 10 25 7 M7 19 Q16 16 25 19"/>
          </g>
        </svg>
        ourlantrixhub.com
      </li>
    </ul>
  </section>
</main>
</body>
</html>
```